Financial Sevices firm looking for Brochure design

Our company Dunmere Halcott and Vesk Limited (DunmereVesk)
i
Is an investment/advisory firm - www.dunmerevesk.com
We invest in the energy sector in Africa and offer advisory services to Energy companies looking to invest in Africa. From oil and gas, to renewables (wind/solar). We are more focused on the "West African" Sub region
We need corporate brochure (Booklet style) to circulate to our corporate clients
We would like to see a design that considers the colours in our Logo (see website)
HI Guys, sorry been travelling. Seen some very good submissions and will be sending updates shortly
Reason: Dear Designers,
Thank you for participating in this project and for some of the great designs i've received so far. Unfortunately, due to the holidays, it has been difficult to consult with other members of my team. As a result, the project deadline is extended by about 12 days
I appreciate your understanding in the situation and looking forward to continuing the excellent collaboration in the coming days
Reason: Hi All,
Apologies for the multiple deadline extensions and thanks so much for all the designs which my team and I will be reviewing today and tomorrow.
We will be closing this project tomorrow by 6pm GMT (17th Jan 2014)
Thanks to all those that submitted such wonderful designs and goodluck!!
Project to be closed finally on 17th Jan 2014 at 6pm GMT
Banks, Investment Firms, Energy companies, Private Equity Funds
I have attached a Brochure that I created myself as an example of the type of information required but please also feel free to visit our website www.dunmerevesk.com
Looking for any creative ideas you have to suplement the information provided.
Financial

```html
<!DOCTYPE html>
<html lang="en">
<head>
<meta charset="utf-8">
<title>DunmereVesk Company Profile – Our Mission</title>
<link rel="stylesheet" href="https://fonts.googleapis.com/css2?family=Roboto:wght@300;400&display=swap">
<style>
  :root {
    --backdrop: #e9e9e9;
    --paper: #ffffff;
    --ink: #3d3d3d;
    --ink-soft: #5a5a5a;
    --accent-red: #d8262d;
    --map-grey: #d9d9d9;
    --pie-grey: #dcdcdc;
    --divider-white: #ffffff;
    --sky-top: #3f5f86;
    --sky-low: #8ea6bf;
    --sea: #4e6a72;
    --rock-dark: #4a3d2c;
    --rock-warm: #8a6a45;
  }
  * { box-sizing: border-box; margin: 0; padding: 0; }
  html, body {
    width: 1200px; height: 840px; overflow: hidden;
    background: var(--backdrop);
    font-family: "Roboto", Arial, sans-serif;
    color: var(--ink);
  }
  .spread {
    position: absolute; left: 30px; top: 20px;
    width: 1140px; height: 800px;
    display: flex;
    box-shadow: 0 6px 24px rgba(0,0,0,0.18);
  }
  .page { position: relative; width: 570px; height: 800px; }
  .page--left { background: var(--paper); }

  .brand {
    position: absolute; top: 36px; right: 40px;
    color: var(--ink); font-size: 18px; font-weight: 400;
  }

  .section-label {
    position: absolute; top: 62px; left: 40px;
    font-size: 12px; font-weight: 300; color: var(--ink-soft);
  }
  .headline {
    position: absolute; top: 120px; left: 40px; width: 500px;
    font-size: 46px; font-weight: 300; line-height: 1.05; color: var(--ink-soft);
    letter-spacing: -0.5px;
  }
  .region-map {
    position: absolute; top: 235px; left: 50px;
    width: 220px; height: 230px;
    background: var(--map-grey);
    border-radius: 46% 54% 38% 62% / 40% 42% 58% 60%;
  }
  .service-pie { position: absolute; top: 255px; left: 320px; width: 170px; height: 170px; }
  .service-pie text { font-family: "Roboto", Arial, sans-serif; font-size: 9.5px; fill: var(--ink-soft); }

  .columns {
    position: absolute; top: 500px; left: 40px; width: 490px;
    display: grid; grid-template-columns: 1fr 1fr; gap: 26px;
  }
  .item { margin-bottom: 18px; }
  .item__title { color: var(--accent-red); font-size: 11px; font-weight: 400; margin-bottom: 3px; }
  .item__body { font-size: 10px; font-weight: 300; line-height: 1.4; color: var(--ink-soft); }
  .item__body li { list-style: none; }

  .folio {
    position: absolute; bottom: 28px; left: 40px;
    font-size: 9px; font-weight: 300; color: var(--ink-soft);
  }

  .page--right { overflow: hidden; }
  .cover-photo {
    position: absolute; inset: 0;
    background: linear-gradient(180deg,
      var(--sky-top) 0%, var(--sky-low) 40%, var(--sea) 48%,
      var(--rock-warm) 62%, var(--rock-dark) 100%);
  }
  .mission-statement {
    position: absolute; top: 36px; left: 250px; width: 260px;
    color: #fff; font-size: 12px; font-weight: 300; line-height: 1.35;
  }
</style>
</head>
<body>
  <main class="spread">
    <section class="page page--left">
      <div class="brand">DunmereVesk</div>
      <p class="section-label">Our Mission</p>
      <h1 class="headline">Developing West Africa</h1>

      <div class="region-map" role="img" aria-label="Map of Africa with project locations marked across West Africa"></div>

      <svg class="service-pie" viewBox="0 0 170 170" role="img" aria-label="Service areas: Advisory, Investment, Project Development">
        <circle cx="85" cy="85" r="80" fill="var(--pie-grey)"/>
        <g stroke="var(--divider-white)" stroke-width="3">
          <line x1="85" y1="85" x2="85" y2="5"/>
          <line x1="85" y1="85" x2="154.3" y2="125"/>
          <line x1="85" y1="85" x2="15.7" y2="125"/>
        </g>
        <text x="30" y="72">Advisory</text>
        <text x="98" y="72">Investment</text>
        <text x="85" y="130" text-anchor="middle">Project</text>
        <text x="85" y="142" text-anchor="middle">Development</text>
      </svg>

      <div class="columns">
        <div>
          <div class="item">
            <h2 class="item__title">Oil &amp; Gas</h2>
            <p class="item__body">Service Provider for an indigenous oil &amp; gas development company contracted by the Nigerian Government to promote industrial development around the oil &amp; gas sector.</p>
          </div>
          <div class="item">
            <h2 class="item__title">Conventional Power</h2>
            <p class="item__body">Financial Adviser to a local power company developing a thermal power plant to boost national generating capacity.</p>
          </div>
          <div class="item">
            <h2 class="item__title">Renewables/Cleantech</h2>
            <p class="item__body">West Africa Adviser and Service Provider to an international specialized fund manager investing in renewable energy and clean technology projects across Africa.</p>
          </div>
        </div>
        <div>
          <div class="item">
            <h2 class="item__title">Advisory</h2>
            <ul class="item__body">
              <li>Project Structuring</li>
              <li>Public Private partnerships</li>
              <li>Privatizations of government owned assets</li>
            </ul>
          </div>
          <div class="item">
            <h2 class="item__title">Investment</h2>
            <ul class="item__body">
              <li>Experience in raising development, construction and long-term debt and equity financing.</li>
              <li>Fundraising</li>
              <li>Portfolio Company Supplementation</li>
            </ul>
          </div>
          <div class="item">
            <h2 class="item__title">Project Development</h2>
            <ul class="item__body">
              <li>Identify, screen, select new project opportunities</li>
              <li>Undertake project preparation and development activities</li>
              <li>Design and negotiate bankable commercial contracts</li>
            </ul>
          </div>
        </div>
      </div>

      <p class="folio">6 | Company Profile</p>
    </section>

    <section class="page page--right">
      <div class="cover-photo" role="img" aria-label="Rocky breakwater running into the sea under a blue sky, with sketched wind turbines drawn above it"></div>
      <p class="mission-statement">We are dedicated to promoting the sustainable implementation of infrastructure and energy related projects in Africa</p>
    </section>
  </main>
</body>
</html>
```